Stationary and biz card for events management company
Plume Events
Stationary and biz card for events management  company - Events
Creative Brief
Professional
Owen Harte
42 Delwyn Street, Southport, Merseyside. PR9 7QT
info@plume-events.co.uk
www.plume-events.co.uk
Please don't include my address on the business card, all contact info to be included on letterhead. I am considering having my business cards printed on the plastic credit card type material. Due to the many finishes available with the plastic cards a unique design may work very well. Please have a look at one of the many plastic card websites, you will see that they do finishes such as matt black or transparent. I am open to ideas as to the finish, the ones I mentioned are just examples.
I'm open to ideas, just the logo or maybe a brief outline of what we do; Event Management, Equipment Hire, Event Packages

```html
<!DOCTYPE html>
<html lang="en">
<head>
<meta charset="utf-8">
<title>Plume Events – Stationery</title>
<link rel="stylesheet" href="https://fonts.googleapis.com/css2?family=Arimo:wght@400;700&display=swap">
<style>
  :root {
    --backdrop: #e9e6e2;
    --paper: #ffffff;
    --brand-red: #d7141c;
    --brand-red-dark: #a50c12;
    --brand-red-light: #f0474d;
    --ink: #1e1e1e;
    --ink-soft: #555555;
    --shadow: rgba(0, 0, 0, 0.18);
  }
  * { box-sizing: border-box; margin: 0; padding: 0; }
  html, body { width: 1200px; height: 600px; overflow: hidden; }
  body {
    background: var(--backdrop);
    font-family: "Arimo", Arial, sans-serif;
    color: var(--ink);
    position: relative;
  }

  /* Business cards */
  .business-card {
    position: absolute;
    left: 40px;
    width: 340px;
    height: 195px;
    background: var(--paper);
    box-shadow: 0 4px 14px var(--shadow);
    overflow: hidden;
  }
  .business-card--first { top: 70px; }
  .business-card--second { top: 320px; }

  .brand-mark {
    display: flex;
    align-items: center;
    gap: 7px;
    color: var(--brand-red);
    font-weight: 700;
    text-transform: uppercase;
    letter-spacing: 0.5px;
  }
  .brand-mark__square {
    background: var(--brand-red);
    flex: none;
  }
  .business-card .brand-mark {
    position: absolute;
    left: 20px;
    top: 30px;
    font-size: 15px;
  }
  .business-card .brand-mark__square { width: 14px; height: 14px; }

  .card-contact {
    position: absolute;
    left: 176px;
    top: 28px;
  }
  .card-contact__name {
    font-size: 16px;
    font-weight: 700;
    text-transform: uppercase;
    letter-spacing: 0.3px;
    margin-bottom: 12px;
  }
  .card-contact__line {
    font-size: 9px;
    line-height: 1.45;
    color: var(--ink);
  }
  .card-contact__line--phone { font-weight: 700; }

  .card-wave {
    position: absolute;
    left: 0;
    bottom: 0;
    width: 340px;
    height: 70px;
  }
  .card-web {
    position: absolute;
    left: 0;
    right: 0;
    bottom: 10px;
    text-align: center;
    color: var(--paper);
    font-size: 9px;
    letter-spacing: 0.4px;
  }

  /* Letterheads */
  .letterhead {
    position: absolute;
    top: 46px;
    width: 360px;
    height: 509px;
    background: var(--paper);
    box-shadow: 0 4px 16px var(--shadow);
    overflow: hidden;
  }
  .letterhead--first { left: 420px; }
  .letterhead--second { left: 805px; }

  .letterhead__band {
    position: absolute;
    left: 0;
    top: 0;
    bottom: 0;
    width: 30px;
    background: linear-gradient(90deg, var(--brand-red-dark) 0%, var(--brand-red) 55%, var(--brand-red-light) 100%);
  }
  .letterhead__band::after {
    content: "";
    position: absolute;
    top: 0;
    bottom: 0;
    right: -6px;
    width: 3px;
    background: var(--brand-red);
  }

  .letterhead .brand-mark {
    position: absolute;
    left: 118px;
    top: 30px;
    font-size: 14px;
  }
  .letterhead .brand-mark__square { width: 13px; height: 13px; }

  .letterhead__address {
    position: absolute;
    left: 270px;
    top: 28px;
    font-size: 6.5px;
    font-weight: 700;
    line-height: 1.5;
    text-transform: uppercase;
    color: var(--ink);
  }
  .letterhead__web {
    position: absolute;
    right: 18px;
    bottom: 14px;
    font-size: 7px;
    color: var(--ink-soft);
  }
</style>
</head>
<body>

  <section class="business-card business-card--first">
    <div class="brand-mark"><span class="brand-mark__square"></span>Plume Events</div>
    <div class="card-contact">
      <p class="card-contact__name">Owen Harte</p>
      <p class="card-contact__line card-contact__line--phone">01704 550183</p>
      <p class="card-contact__line card-contact__line--phone">07700 900417</p>
      <p class="card-contact__line">info@plume-events.co.uk</p>
    </div>
    <svg class="card-wave" viewBox="0 0 340 70" preserveAspectRatio="none" aria-hidden="true">
      <path d="M0 22 C90 48 210 0 340 18 L340 70 L0 70 Z" fill="#f2b3b5"/>
      <path d="M0 32 C100 56 220 10 340 28 L340 70 L0 70 Z" fill="#d7141c"/>
      <path d="M0 50 C110 66 230 34 340 48 L340 70 L0 70 Z" fill="#a50c12"/>
    </svg>
    <p class="card-web">www.plume-events.co.uk</p>
  </section>

  <section class="business-card business-card--second">
    <div class="brand-mark"><span class="brand-mark__square"></span>Plume Events</div>
    <div class="card-contact">
      <p class="card-contact__name">Owen Harte</p>
      <p class="card-contact__line card-contact__line--phone">01704 550183</p>
      <p class="card-contact__line card-contact__line--phone">07700 900417</p>
      <p class="card-contact__line">info@plume-events.co.uk</p>
    </div>
    <svg class="card-wave" viewBox="0 0 340 70" preserveAspectRatio="none" aria-hidden="true">
      <path d="M0 22 C90 48 210 0 340 18 L340 70 L0 70 Z" fill="#f2b3b5"/>
      <path d="M0 32 C100 56 220 10 340 28 L340 70 L0 70 Z" fill="#d7141c"/>
      <path d="M0 50 C110 66 230 34 340 48 L340 70 L0 70 Z" fill="#a50c12"/>
    </svg>
    <p class="card-web">www.plume-events.co.uk</p>
  </section>

  <section class="letterhead letterhead--first">
    <div class="letterhead__band"></div>
    <div class="brand-mark"><span class="brand-mark__square"></span>Plume Events</div>
    <address class="letterhead__address">
      42 Delwyn Street,<br>Southport,<br>Merseyside.<br>PR9 7QT
    </address>
    <p class="letterhead__web">www.plume-events.co.uk</p>
  </section>

  <section class="letterhead letterhead--second">
    <div class="letterhead__band"></div>
    <div class="brand-mark"><span class="brand-mark__square"></span>Plume Events</div>
    <address class="letterhead__address">
      42 Delwyn Street,<br>Southport,<br>Merseyside.<br>PR9 7QT
    </address>
    <p class="letterhead__web">www.plume-events.co.uk</p>
  </section>

</body>
</html>
```